Renewable Energy Consultancy needs relatively simple but smart website

We are a renewable energy focussed consultancy called Bellmoran, and we are just starting out. Our target is to bring knowledge of the detailed technical and commercial operations of renewables projects, mainly wind energy.

Our target customers are major energy utilities and private finance groups, who look to invest in renewables projects as a long term money-earning system. We are a fairly young, dynamic team of industry-respected people (4 of us) but we need to make ourselves look bigger than this (our customers will expect us to take on major projects, so we need to look big enough to handle it...)

We're not going to sell anything from our website and we expect it to just support our company name. Most of our customers are made by strong networks and relationships, so its mainly there to give confidence in our capabilities and give a strong view of who we are. We probably need a site with 4/5 pages which we can then expand when needed.

We have logos and headers (attached) which we want to use (also run through artpitchly), and I've attached a few pictures of projects similar to those we will be involved in to give us a feel for how it will look. Also attached are the colours we liked which are now used in the logo, and the font details. Whilst we're a "green" company with a "green" logo, we don't want to be completely green, so some nice combinations of colours on the pages would be good.

Ideally we need to have chirpnet/workgrid news feeds somewhere linked into the site.

The design should be smart - giving a feel of high integrity and assurance whilst making us seem approachable and knowledgeable.

Target Market(s)

Renewables investors, developers of renewables projects (wind farms etc),

Industry/Entity Type

Finance

Coding

Coded - Design and coding required

Number of Pages Required

4 page

Other font styles liked:
• See the attachment with brand text/colour details ("colour codes" filename)

Requirements
Must have
• A fairly simple, but smart website design. We're looking to provide confidence and consolidate our networks with the website, not specifically find new customers - so its really just to give customers somewhere they can relate to online
Nice to have
• We have logos/brands and colours - so a website which incorperates these well and brings accross a professional company
• Would be nice to have a page (such as a blog/wordpress) we can easily update with news/events etc and links to chirpnet feed and workgrid feed ideally.
Should not have
• cartoons, flashy gimmicks,

```html
<!DOCTYPE html>
<html lang="en">
<head>
<meta charset="utf-8">
<title>Bellmoran — Renewable Energy Focussed Consultancy</title>
<link href="https://fonts.googleapis.com/css2?family=Lato:wght@300;400;700;900&family=Questrial&display=swap" rel="stylesheet">
<style>
:root{
  --green:#4e8f0c;
  --green-text:#5c9a17;
  --dark:#3f4040;
  --ink:#222;
  --muted:#555;
  --footer-bg:#eeeeee;
  --feed-blue:#1fa3df;
  --feed-navy:#17375e;
  --white:#fff;
}
*{box-sizing:border-box;margin:0;padding:0}
html,body{width:729px;height:1200px;overflow:hidden;background:var(--white)}
body{font-family:'Lato',sans-serif;color:var(--ink);position:relative}
.abs{position:absolute}

/* top bar */
.topbar{left:0;top:0;width:729px;height:58px;background:var(--green)}
.connect{left:129px;top:11px;font-size:7px;color:var(--white);display:flex;gap:8px;align-items:center}
.connect b{font-weight:700;font-size:7px}
.phone{left:466px;top:9px;font-size:9.5px;color:var(--white);display:flex;align-items:center;gap:5px}
.email-pill{left:546px;top:8px;width:62px;height:15px;border-radius:8px;background:#111;color:var(--white);font-size:6.5px;display:flex;align-items:center;justify-content:center;gap:5px;letter-spacing:.3px}

/* nav */
.navbox{left:121px;top:29px;width:487px;height:55px;border-radius:16px;background:linear-gradient(#ffffff,#e9e9e9);box-shadow:0 1px 3px rgba(0,0,0,.15);z-index:2}
.brand{left:8px;top:14px;display:flex;align-items:center;gap:8px}
.brand-dot{width:24px;height:24px;border-radius:50%;background:var(--green)}
.brand-name{font-family:'Questrial',sans-serif;font-size:22px;color:#555;letter-spacing:1px;border-left:1px solid #aaa;padding-left:7px}
.nav{left:203px;top:20px;display:flex;gap:0;font-family:'Questrial',sans-serif;font-size:8.2px;color:var(--ink)}
.nav span{margin-right:13px}
.nav .active{color:var(--green-text)}

/* hero */
.hero{left:0;top:58px;width:729px;height:335px;background:linear-gradient(180deg,#b9c7d6 0%,#d9dde2 35%,#8b8f94 60%,#6f3a33 78%,#3b3634 100%)}
.hero-panel{left:129px;top:146px;width:175px;height:131px;background:rgba(40,40,40,.85);padding:20px 0 0 16px;line-height:24px}
.hero-panel .strong{font-family:'Lato',sans-serif;font-weight:700;font-size:25px;color:#7bc21c;display:block;line-height:23px}
.hero-panel .light{font-family:'Questrial',sans-serif;font-size:24px;color:var(--white);display:block;line-height:23px}
.dots{left:342px;top:367px;display:flex;gap:5px}
.dots i{width:7px;height:7px;border-radius:50%;border:1.4px solid var(--white);display:block}
.dots i.on{border-color:#7bc21c}

/* services */
.service{top:419px;width:107px}
.tile{height:63px;position:relative;color:var(--white)}
.tile.green{background:var(--green)}
.tile.grey{background:var(--dark)}
.tile .label{position:absolute;left:10px;bottom:7px;font-size:9px}
.tile .plus{position:absolute;right:5px;bottom:8px;width:6px;height:6px;background:var(--white)}
.tile .plus::after{content:"+";position:absolute;left:0;top:-3px;font-size:7px;color:var(--dark);line-height:10px;width:6px;text-align:center;font-weight:700}
.tile svg{position:absolute;right:24px;top:9px}
.service p{font-size:6.3px;line-height:12px;color:var(--muted);margin-top:6px}

/* section headers */
.sec-head{height:37px;background:var(--green);color:var(--white);font-size:12.5px;padding:0 7px;display:flex;align-items:center;justify-content:space-between;letter-spacing:.3px}
.arrows{display:flex;gap:8px;font-size:13px;font-weight:300}

.project-img{left:128px;top:642px;width:270px;height:136px;background:linear-gradient(180deg,#7fb0e0 0%,#3d6fa8 35%,#1c4a7e 100%)}
.project-cap{left:128px;top:744px;width:270px;height:34px;background:rgba(30,30,30,.85);color:var(--white);font-size:8.5px;padding:12px 14px}

.testimonials{left:128px;top:790px;width:270px;height:140px;background:var(--green);color:var(--white);padding:12px 11px}
.testimonials h3{font-weight:400;font-size:12px;letter-spacing:.3px}
.avatar{left:12px;top:37px;width:54px;height:54px;border-radius:50%;background:radial-gradient(circle at 50% 40%,#c59a7c,#6d8fa8);border:2px solid var(--white)}
.t-name{left:73px;top:54px;font-weight:900;font-size:8.5px}
.t-co{left:73px;top:68px;font-size:6.5px}
.t-quote{left:12px;top:99px;width:250px;font-size:6.8px;line-height:12px}

/* news */
.news{left:413px;width:188px}
.date{width:49px;height:43px;background:var(--dark);color:var(--white);text-align:center;font-size:9.5px;line-height:11px;padding-top:6px}
.date b{font-weight:700}
.news-title{left:57px;top:1px;width:130px;font-size:8.8px;font-weight:700;line-height:12px}
.news-body{left:0;top:54px;width:188px;font-size:6.3px;line-height:12px;color:var(--muted)}
.news-body em{color:var(--green-text);font-style:italic}

/* invest band */
.band{left:0;top:963px;width:729px;height:46px;background:var(--dark);color:var(--white)}
.band p{position:absolute;left:128px;top:9px;width:330px;font-size:9.4px;line-height:15px;letter-spacing:-.2px}
.invest{left:474px;top:11px;width:114px;height:26px;background:var(--green);font-size:9.5px;font-weight:700;display:flex;align-items:center;justify-content:center;letter-spacing:-.2px}

/* footer */
.footer{left:0;top:1009px;width:729px;height:191px;background:var(--footer-bg)}
.fcol{top:21px}
.fcol h4{font-weight:400;font-size:9px;color:var(--green-text);margin-bottom:13px}
.fcol li{list-style:none;font-size:6.6px;line-height:15.2px;color:var(--ink)}
.feed{left:413px;width:188px;height:60px;color:var(--white);padding:8px 12px}
.feed.chirp{top:20px;background:var(--feed-blue)}
.feed.grid{top:84px;background:var(--feed-navy)}
.feed .fname{display:flex;align-items:center;gap:6px;font-size:8.5px}
.feed .fname i{width:8px;height:8px;border-radius:50%;background:var(--white);display:block}
.feed .ftext{font-size:6.2px;line-height:12px;margin:6px 0 0 28px;opacity:.85}
.feed .ftime{position:absolute;right:3px;bottom:5px;font-size:6.3px}
.feed .farrows{position:absolute;right:7px;top:6px;font-size:8px}
.copy-line{left:0;top:162px;width:729px;height:1px;background:#ccc}
.copyright{left:0;top:172px;width:729px;text-align:center;font-size:6.5px;color:var(--ink)}
</style>
</head>
<body>

<header>
  <div class="abs topbar"></div>
  <div class="abs connect">Connect With Us <b>chirpnet</b> <b>workgrid</b></div>
  <div class="abs phone">
    <svg width="7" height="7" viewBox="0 0 10 10"><path d="M2 0.5 3.8 2.8 2.8 4a6 6 0 0 0 3.2 3.2l1.2-1 2.3 1.8-1 1.5C5 9.8 0.2 5 0.5 1.5Z" fill="#fff"/></svg>
    (415)555-0147
  </div>
  <div class="abs email-pill">
    <svg width="8" height="6" viewBox="0 0 8 6"><rect x=".5" y=".5" width="7" height="5" fill="none" stroke="#7bc21c"/><path d="M.5.5 4 3.3 7.5.5" fill="none" stroke="#7bc21c"/></svg>
    E-MAIL
  </div>

  <nav class="abs navbox">
    <div class="abs brand"><span class="brand-dot"></span><span class="brand-name">Bellmoran</span></div>
    <div class="abs nav">
      <span class="active">Home</span><span>About us</span><span>Case studies</span><span>Services</span><span>Media</span><span>Contact us</span>
    </div>
  </nav>
</header>

<section>
  <div class="abs hero" role="img" aria-label="Offshore wind installation vessel in harbour with wind turbines under a bright sky"></div>
  <div class="abs hero-panel">
    <span class="strong">Renewable</span>
    <span class="strong">Energy</span>
    <span class="light">Focussed</span>
    <span class="light">Consultancy</span>
  </div>
  <div class="abs dots"><i class="on"></i><i></i><i></i><i></i></div>
</section>

<section>
  <div class="abs service" style="left:128px">
    <div class="tile green">
      <svg width="44" height="44" viewBox="0 0 44 44" fill="#fff">
        <rect x="13" y="14" width="3" height="28"/><path d="M14.5 14 12 0h5z"/><path d="M14.5 14 2 22l2 3z"/><path d="M14.5 14 27 22l-2 3z"/>
        <rect x="31" y="24" width="2.4" height="18"/><path d="M32 24 30 14h4z"/><path d="M32 24 23 29l1.5 2z"/><path d="M32 24 41 29l-1.5 2z"/>
      </svg>
      <span class="label">Wind</span><span class="plus"></span>
    </div>
    <p>Lorem Ipsum is simply dummy text of the printing and typesetting industry. Lorem Ipsum has been the industry's standard dummy text ever since the 1500s.</p>
  </div>
  <div class="abs service" style="left:250px">
    <div class="tile grey">
      <svg width="50" height="46" viewBox="0 0 50 46" fill="none" stroke="#fff" stroke-width="2">
        <path d="M6 16h34l-4 18H2z"/><path d="M4 25h34M14 16l-4 18M24 16l-4 18M33 16l-4 18"/>
        <path d="M20 34v8M12 43h16"/><circle cx="42" cy="9" r="3"/><path d="M42 1v3M48 9h-3M47 4l-2 2M37 4l2 2"/>
      </svg>
      <span class="label">Solar</span><span class="plus"></span>
    </div>
    <p>Lorem Ipsum is simply dummy text of the printing and typesetting industry. Lorem Ipsum has been the industry's standard dummy text ever since the 1500s.</p>
  </div>
  <div class="abs service" style="left:372px">
    <div class="tile grey">
      <svg width="44" height="46" viewBox="0 0 44 46" fill="none" stroke="#fff" stroke-width="3" stroke-linecap="round">
        <circle cx="22" cy="16" r="3" fill="#fff" stroke="none"/><path d="M22 19v24"/>
        <path d="M15 9a10 10 0 0 0 0 14M29 9a10 10 0 0 1 0 14M9 4a17 17 0 0 0 0 24M35 4a17 17 0 0 1 0 24"/>
      </svg>
      <span class="label">Transmission</span><span class="plus"></span>
    </div>
    <p>Lorem Ipsum is simply dummy text of the printing and typesetting industry. Lorem Ipsum has been the industry's standard dummy text ever since the 1500s.</p>
  </div>
  <div class="abs service" style="left:494px">
    <div class="tile grey">
      <svg width="30" height="46" viewBox="0 0 30 46" fill="#fff" style="right:10px"><path d="M20 0 4 26h10L8 46 26 18H15z"/></svg>
      <span class="label">Energy Storage</span><span class="plus"></span>
    </div>
    <p>Lorem Ipsum is simply dummy text of the printing and typesetting industry. Lorem Ipsum has been the industry's standard dummy text ever since the 1500s.</p>
  </div>
</section>

<section>
  <div class="abs sec-head" style="left:128px;top:594px;width:270px">PROJECTS <span class="arrows"><span>&lsaquo;</span><span>&rsaquo;</span></span></div>
  <div class="abs project-img" role="img" aria-label="Offshore wind farm turbines standing in the open sea"></div>
  <div class="abs project-cap">Neque porro quisquam est qui dolorem ipsum quia dolor</div>

  <div class="abs testimonials">
    <h3>TESTIMONIALS</h3>
    <div class="abs avatar" role="img" aria-label="Client portrait"></div>
    <div class="abs t-name">DANIEL HARWOOD</div>
    <div class="abs t-co">Company Name</div>
    <p class="abs t-quote">Sed ut perspiciatis unde omnis iste natus error sit voluptatem accusantium doloremque laudantium, totam rem aperiam, eaque ipsa quae ab illo inventore veritatis et quasi architecto beatae vitae dicta sunt explicabo.</p>
  </div>

  <div class="abs sec-head" style="left:413px;top:594px;width:188px">LATEST NEWS <span class="arrows"><span>&lsaquo;</span><span>&rsaquo;</span></span></div>

  <article class="abs news" style="top:642px">
    <div class="date">5TH<br><b>MARCH</b><br>2015</div>
    <h4 class="abs news-title">Lorem Ipsum is simply dummy text of the printing and typesetting industry.</h4>
    <p class="abs news-body">Lorem Ipsum is simply dummy text of the printing and typesetting industry. Lorem Ipsum has been the industry's standard dummy text ever since the 1500s Lorem Ipsum is simply dummy text of the printing and typesetting industry. Lorem Ipsum has been the industry's standard dummy text ever since the 1500s &nbsp;... <em>Read More</em></p>
  </article>
  <article class="abs news" style="top:807px">
    <div class="date">5TH<br><b>MARCH</b><br>2015</div>
    <h4 class="abs news-title">Lorem Ipsum is simply dummy text of the printing and typesetting industry.</h4>
    <p class="abs news-body">Lorem Ipsum is simply dummy text of the printing and typesetting industry. Lorem Ipsum has been the industry's standard dummy text ever since the 1500s Lorem Ipsum is simply dummy text of the printing and typesetting industry. Lorem Ipsum has been the industry's standard dummy text ever since the 1500s &nbsp;... <em>Read More</em></p>
  </article>
</section>

<section class="abs band">
  <p>Our customers are major energy utilities and private finance groups, who look to invest in renewables projects as a long term money-earning system</p>
  <div class="abs invest">Invest Now !</div>
</section>

<footer class="abs footer">
  <div class="abs fcol" style="left:128px">
    <h4>Menu Links</h4>
    <ul><li>Home</li><li>About</li><li>Classes</li><li>Locations</li><li>TD Store</li><li>Range</li><li>Contact Us</li></ul>
  </div>
  <div class="abs fcol" style="left:194px">
    <h4>Support Links</h4>
    <ul><li>Site Map</li><li>Privacy Policy</li><li>Terms and Conditions</li></ul>
  </div>
  <div class="abs fcol" style="left:273px">
    <h4>Contact Us</h4>
    <ul><li>Kestrel Partners</li><li>Lindenweg 42b</li><li>10115 Berlin</li><li>Germany</li><li>Telephone: +49 30 5550 1928</li><li>E-mail: hello@bellmoran-mail.de</li></ul>
  </div>

  <div class="abs feed chirp">
    <div class="fname"><i></i>chirpnet</div>
    <p class="ftext">Lorem Ipsum is simply dummy text of the printing and typesetting industry.</p>
    <span class="farrows">&lsaquo; &rsaquo;</span>
    <span class="ftime">2h 30 Mints</span>
  </div>
  <div class="abs feed grid">
    <div class="fname"><i></i>workgrid</div>
    <p class="ftext">Lorem Ipsum is simply dummy text of the printing and typesetting industry.</p>
    <span class="farrows">&lsaquo; &rsaquo;</span>
    <span class="ftime">2h 30 Mints</span>
  </div>

  <div class="abs copy-line"></div>
  <div class="abs copyright">© 2015 Company Name ,All Rights Reserved</div>
</footer>

</body>
</html>
```